Banner für eBook/ Hörbuch
Zielgruppe
ihrFALKE ist das größte deutschsprachige Portal rund um die Themen innere Ruhe und Selbstverwirklichung.
ihrFALKE verzeichnet über 200.000 Besucher pro Monat. Über 40.000 Plauderhof-Fans folgenden ihrFALKE.
Das eBook 'Sieben Wege zu einem klaren Kopf am Morgen' wird über ihrFALKE vertrieben (http://ihrfalke.de/sieben-wege/) und hat sich bereits über 1.000 Mal verkauft. Das Buch ist auch als Hörbuch erhältlich.
Aufgabenstellung
Zur Vermarktung unseres eBooks/ Hörbuchs testen wir aktuell 2 Integrationsvarianten auf ihrfalke.de, einen Banner oberhalb des Blogs, einen rechts der Blogeinträge. Der obere Banner zeigt aktuell deutlich geringere CTRs und wir wollen weitere Banner-Varianten für diesen Bannerplatz testen.
Wir vermuten, dass der obere Banner aktuell nicht genug Bezug zu ihrFALKE und zum Autor "Ole" hat. Oder anders: Wir glauben, dass der aktuelle Banner wie ein normaler Banner für ein externes Produkt wirkt.
Daher wollen wir eine oder mehrere Banner-Alternativen testen, die
- einen klaren Wiedererkennungswert zu ihrFALKE und/oder zum Autor "Ole" herstellen (durch Farbauswahl, Einbindung unseres Logo-Mönchs, "mein neues Buch")
- einen agressiveren Call-to-Action beinhalten (hier kann auch das Thema "bereits über 1.000 Mal verkauft" gespielt werden)
- herausstellen, dass das Buch als eBook und Hörbuch zu haben ist
Die Abmessungen des Banners sind 650 x 230 Pixel.
Melden Sie sich bitte jederzeit bei Fragen.
Lars Böttcher

```html
<!DOCTYPE html>
<html lang="de">
<head>
<meta charset="utf-8">
<title>ihrFALKE – Sieben Wege zu einem klaren Kopf am Morgen</title>
<link rel="stylesheet" href="https://fonts.googleapis.com/css2?family=Cinzel:wght@400;700&family=Open+Sans:wght@400;600;700;800&display=swap">
<style>
  :root {
    --canvas: #e4dad9;
    --shelf-light: #f4f4f4;
    --shelf-dark: #d2d2d2;
    --book-face: #f7f7f7;
    --book-edge: #c9c9c9;
    --cover-ink: #3a3a3a;
    --cover-accent: #a0256f;
    --figure-tone: #e2e0dd;
    --plum: #5c1a3d;
    --magenta: #a0256f;
    --magenta-deep: #8e1d61;
    --rose: #c98cbb;
    --rose-light: #d9a5cd;
    --ink: #3b0f28;
    --white: #ffffff;
  }
  * { margin: 0; padding: 0; box-sizing: border-box; }
  html, body { width: 1200px; height: 425px; overflow: hidden; background: var(--canvas); }
  .banner {
    position: relative;
    width: 1200px; height: 425px;
    background: var(--canvas);
    overflow: hidden;
    font-family: "Open Sans", Arial, sans-serif;
  }

  /* Buch */
  .book-stage {
    position: absolute; left: 0; top: 0;
    width: 330px; height: 425px;
    background: linear-gradient(90deg, var(--shelf-dark) 0%, var(--shelf-light) 55%, #e4e4e4 100%);
  }
  .book-cover {
    position: absolute; left: 30px; top: 18px;
    width: 248px; height: 380px;
    background: linear-gradient(90deg, var(--book-edge) 0%, var(--book-face) 7%, var(--book-face) 100%);
    box-shadow: 10px 8px 22px rgba(0,0,0,.2);
    text-align: center;
    font-family: "Cinzel", "Times New Roman", serif;
    color: var(--cover-ink);
  }
  .book-cover__author { position: absolute; top: 26px; left: 0; right: 0; font-size: 10px; letter-spacing: 1px; }
  .book-cover__title { position: absolute; top: 54px; left: 22px; right: 14px; font-size: 17px; line-height: 1.35; font-weight: 400; }
  .book-cover__figure { position: absolute; top: 170px; left: 104px; width: 46px; height: 86px; background: var(--figure-tone); border-radius: 4px; }
  .book-cover__tagline { position: absolute; top: 274px; left: 0; right: 0; color: var(--cover-accent); line-height: 1.2; }
  .book-cover__tagline small { display: block; font-size: 9px; }
  .book-cover__tagline span { display: block; font-size: 15px; }
  .book-cover__brand { position: absolute; bottom: 14px; left: 0; right: 0; font-family: "Open Sans", Arial, sans-serif; font-size: 9px; font-weight: 700; color: var(--cover-ink); }

  .divider { position: absolute; left: 0; top: 0; }

  /* Headline */
  .headline {
    position: absolute; left: 348px; top: 152px;
    font-family: "Cinzel", "Times New Roman", serif;
    line-height: 1;
  }
  .headline__lead { display: block; color: var(--plum); font-size: 40px; font-weight: 700; letter-spacing: 1px; }
  .headline__main { display: block; margin-top: 14px; color: var(--magenta); font-size: 57px; font-weight: 400; letter-spacing: 2px; }

  /* Call to Action */
  .cta {
    position: absolute; left: 437px; top: 306px;
    width: 338px; height: 62px;
    display: flex; text-decoration: none;
    background: var(--rose);
  }
  .cta__icon { width: 64px; height: 62px; background: var(--magenta-deep); display: flex; align-items: center; justify-content: center; }
  .cta__label { flex: 1; display: flex; align-items: center; justify-content: center; color: var(--ink); font-size: 20px; font-weight: 800; letter-spacing: .3px; white-space: nowrap; }

  /* Siegel */
  .seal { position: absolute; left: 870px; top: 0; }
  .seal__text { position: absolute; left: 951px; width: 157px; text-align: center; line-height: 1.12; }
  .seal__sold { top: 26px; color: var(--ink); font-size: 29px; }
  .seal__sold strong { font-weight: 800; font-size: 27px; }
  .seal__new { top: 238px; color: var(--white); font-size: 24px; font-weight: 700; }
  .seal__brand { display: block; font-size: 30px; font-weight: 800; margin: 6px 0 2px; }
  .seal__book { display: block; font-size: 30px; font-weight: 700; }
</style>
</head>
<body>
<main class="banner">
  <section class="book-stage">
    <div class="book-cover">
      <p class="book-cover__author">OLE BRANDMEYER</p>
      <h2 class="book-cover__title">SIEBEN WEGE ZU EINEM KLAREN KOPF AM MORGEN</h2>
      <div class="book-cover__figure" role="img" aria-label="Gezeichneter Mönch in Meditationshaltung"></div>
      <p class="book-cover__tagline"><small>GELASSEN UND FOKUSSIERT</small><span>ZIELE ERREICHEN</span></p>
      <p class="book-cover__brand">ihrFALKE</p>
    </div>
  </section>

  <svg class="divider" width="360" height="425" viewBox="0 0 360 425" aria-hidden="true">
    <rect x="328" y="0" width="5" height="425" fill="var(--magenta)"/>
    <polygon points="333,161 351,175 333,189" fill="var(--magenta)"/>
  </svg>

  <h1 class="headline">
    <span class="headline__lead">Gelassen &amp; Fokussiert</span>
    <span class="headline__main">Ziele erreichen</span>
  </h1>

  <a class="cta" href="http://ihrfalke.de/sieben-wege/">
    <span class="cta__icon">
      <svg width="30" height="20" viewBox="0 0 30 20" aria-hidden="true">
        <path d="M1 10 Q15 -4 29 10 Q15 24 1 10 Z" fill="var(--white)"/>
        <circle cx="15" cy="10" r="5" fill="var(--magenta-deep)"/>
        <circle cx="15" cy="10" r="2" fill="var(--white)"/>
      </svg>
    </span>
    <span class="cta__label">eBOOK &amp; HÖRBUCH HOLEN</span>
  </a>

  <svg class="seal" width="330" height="425" viewBox="870 0 330 425" aria-hidden="true">
    <circle cx="1029" cy="185" r="138" fill="none" stroke="var(--magenta)" stroke-width="14" stroke-linecap="round" stroke-dasharray="0 14.4"/>
    <circle cx="1029" cy="185" r="136" fill="var(--magenta)"/>
    <circle cx="1029" cy="185" r="124" fill="none" stroke="var(--rose-light)" stroke-width="2" stroke-dasharray="3 4"/>
    <rect x="951" y="10" width="157" height="186" fill="var(--rose-light)"/>
    <polygon points="951,196 1108,196 1108,415 1029,390 951,415" fill="var(--magenta-deep)"/>
    <line x1="951" y1="196" x2="1108" y2="196" stroke="var(--white)" stroke-width="2"/>
  </svg>
  <p class="seal__text seal__sold">Schon<br>1.000 Mal<br><strong>VERKAUFT</strong></p>
  <p class="seal__text seal__new">DAS NEUE<span class="seal__brand">ihrFALKE</span><span class="seal__book">Buch</span></p>
</main>
</body>
</html>
```